Ginger Beer Can Design for a none alcoholic bavarage

We need a cool, modern, fresh design for a can.

- 330ml sleek can size
- 0.0% alcohol
- BIO
- ingredience: Water, Sugar, Ginger, limejuice, Gummi Arabicum, Carbonisation
- Energy table of fats, carbs, protein, etc.
- address: Quiet Meadow Drinks, Lindenweg 42, 4052 Basel

```html
<!DOCTYPE html>
<html lang="en">
<head>
<meta charset="utf-8">
<title>Concept 8 – Playful Geometric</title>
<link href="https://fonts.googleapis.com/css2?family=Rubik:wght@500;700;800;900&family=Nunito+Sans:wght@400;600;700&display=swap" rel="stylesheet">
<style>
:root{
  --paper:#f7f5ee;
  --cream:#f8f6ea;
  --ink:#1f3d31;
  --green:#4ea56b;
  --lime:#9ccb4f;
  --lime-soft:#bedd7e;
  --mint:#7fc7a2;
  --teal:#9fd3cb;
  --yellow:#f6d65c;
  --line:#c9cfc4;
  --white:#ffffff;
}
*{box-sizing:border-box;margin:0;padding:0}
html,body{width:1200px;height:675px;overflow:hidden;background:var(--paper)}
body{position:relative;font-family:"Nunito Sans",sans-serif;color:var(--ink)}

.concept-label{position:absolute;left:36px;top:32px;font:700 17px "Rubik",sans-serif;letter-spacing:2px;color:var(--green)}
.concept-title{position:absolute;left:34px;top:54px;font:900 54px/1 "Rubik",sans-serif;letter-spacing:1px;color:var(--ink)}
.title-rule{position:absolute;left:36px;top:134px;width:66px;height:1px;background:var(--ink);opacity:.5}
.concept-intro{position:absolute;left:36px;top:146px;width:320px;font-size:11px;line-height:1.45}

.feature-list{position:absolute;right:40px;top:40px;display:flex}
.feature{width:104px;text-align:center;border-left:1px solid var(--line)}
.feature:first-child{border-left:none}
.feature svg{width:52px;height:52px;display:block;margin:0 auto 6px}
.feature-name{font:600 11px "Nunito Sans",sans-serif;letter-spacing:.5px;color:var(--ink)}
.feature-sub{font-size:7.5px;letter-spacing:.4px;color:var(--ink);text-transform:uppercase}

.panel-caption{position:absolute;top:204px;font:700 10px "Nunito Sans",sans-serif;letter-spacing:.8px;color:var(--green)}
.panel-caption.back{left:140px}
.panel-caption.front{left:440px}

.label-sheet{position:absolute;left:34px;top:222px;width:672px;height:442px;border:1px solid #999;background:var(--cream);overflow:hidden;display:flex}
.back-panel,.front-panel{position:relative;height:100%;overflow:hidden}
.back-panel{width:302px;border-right:1px dashed var(--line)}
.front-panel{width:370px}
.deco{position:absolute;border-radius:50%}

.ingredients{position:absolute;left:84px;top:30px;width:180px;font-size:9px;line-height:1.35}
.ingredients b{font-weight:700}
.nutri-title{position:absolute;left:82px;top:92px;font:700 7.5px "Nunito Sans",sans-serif;color:var(--green)}
.nutri-table{position:absolute;left:82px;top:104px;width:152px;border:1px solid #777;border-collapse:collapse;font-size:7.5px;background:var(--white)}
.nutri-table td{padding:2px 4px;border-bottom:1px solid #bbb}
.nutri-table td:last-child{text-align:right}
.nutri-table .sub td:first-child{padding-left:14px}
.address{position:absolute;left:84px;top:222px;display:flex;gap:8px;font-size:8px;line-height:1.4}
.address svg{width:14px;height:18px;flex:none;margin-top:2px}
.back-rule{position:absolute;left:82px;top:278px;width:152px;height:1px;background:var(--line)}
.cert-row{position:absolute;left:82px;top:290px;display:flex;gap:14px}
.cert{width:44px;text-align:center;font:700 7px "Nunito Sans",sans-serif}
.cert-shape{width:36px;height:36px;margin:0 auto 6px}

.brand-disc{position:absolute;left:62px;top:60px;width:262px;height:262px;border-radius:50%;background:var(--white)}
.brand-name{position:absolute;left:0;width:370px;top:100px;text-align:center;font:900 44px/0.98 "Rubik",sans-serif;color:var(--ink);letter-spacing:.5px}
.flavour{position:absolute;left:0;width:370px;top:254px;text-align:center;font:800 22px "Rubik",sans-serif;color:var(--lime);letter-spacing:1px}
.badge-row{position:absolute;left:100px;top:296px;display:flex;align-items:center;gap:8px}
.badge{width:50px;height:50px;border:2px solid var(--green);border-radius:50%;background:var(--white);display:flex;flex-direction:column;align-items:center;justify-content:center;color:var(--ink)}
.badge strong{font:700 12px "Rubik",sans-serif}
.badge small{font-size:6px;font-weight:700}
.badge.bio strong{font-size:15px;color:var(--green)}
.fruit-art{width:76px;height:50px;border-radius:40% 50% 45% 50%;background:linear-gradient(120deg,#f1e3b6 0%,#e8cf8a 45%,#c8dc6a 70%,#f6d65c 100%)}
.product-band{position:absolute;left:88px;top:364px;width:208px;padding:3px 0;background:var(--lime-soft);text-align:center;font:700 10.5px/1.25 "Rubik",sans-serif;color:var(--ink);letter-spacing:.5px}
.volume{position:absolute;left:0;width:370px;top:402px;text-align:center;font:600 17px "Nunito Sans",sans-serif}
</style>
</head>
<body>

<p class="concept-label">CONCEPT 8</p>
<h1 class="concept-title">PLAYFUL GEOMETRIC</h1>
<div class="title-rule"></div>
<p class="concept-intro">A lively and modern design that uses bold geometric shapes, fresh colors and clean iconography to create a youthful, energetic and refreshing look.</p>

<ul class="feature-list">
  <li class="feature" style="list-style:none">
    <svg viewBox="0 0 52 52"><circle cx="26" cy="26" r="24" fill="none" stroke="#1f3d31" stroke-width="1"/><path d="M18 36 C18 22 28 16 36 15 C36 26 30 34 18 36Z" fill="#7fc7a2" stroke="#1f3d31" stroke-width="1"/><path d="M18 36 L32 20" stroke="#1f3d31" stroke-width="1"/></svg>
    <p class="feature-name">BIO</p><p class="feature-sub">Organic<br>ingredients</p>
  </li>
  <li class="feature" style="list-style:none">
    <svg viewBox="0 0 52 52"><circle cx="26" cy="26" r="24" fill="none" stroke="#1f3d31" stroke-width="1"/><path d="M17 16 L25 37 L35 16" fill="none" stroke="#4ea56b" stroke-width="2"/></svg>
    <p class="feature-name">VEGAN</p><p class="feature-sub">Friendly</p>
  </li>
  <li class="feature" style="list-style:none">
    <svg viewBox="0 0 52 52"><circle cx="26" cy="26" r="24" fill="none" stroke="#1f3d31" stroke-width="1"/><circle cx="20" cy="32" r="4" fill="none" stroke="#1f3d31"/><circle cx="30" cy="27" r="3.5" fill="none" stroke="#1f3d31"/><circle cx="28" cy="17" r="2.5" fill="none" stroke="#1f3d31"/><circle cx="33" cy="36" r="2" fill="none" stroke="#1f3d31"/></svg>
    <p class="feature-name">SPARKLING</p><p class="feature-sub">Refreshment</p>
  </li>
  <li class="feature" style="list-style:none">
    <svg viewBox="0 0 52 52"><circle cx="26" cy="26" r="24" fill="none" stroke="#1f3d31" stroke-width="1"/><circle cx="26" cy="28" r="11" fill="#bedd7e" stroke="#4ea56b" stroke-width="1.5"/><path d="M26 17V39M15 28H37M18 20L34 36M34 20L18 36" stroke="#f8f6ea" stroke-width="1"/></svg>
    <p class="feature-name">REAL GINGER</p><p class="feature-sub">Real lime</p>
  </li>
</ul>

<p class="panel-caption back">BACK PANEL</p>
<p class="panel-caption front">FRONT PANEL</p>

<section class="label-sheet">
  <div class="back-panel">
    <span class="deco" style="left:178px;top:-60px;width:96px;height:96px;background:var(--mint);opacity:.8"></span>
    <span class="deco" style="left:-14px;top:22px;width:40px;height:40px;background:var(--lime-soft);opacity:.6"></span>
    <span class="deco" style="left:-20px;top:130px;width:30px;height:200px;border-radius:0;background:var(--mint);opacity:.6"></span>
    <span class="deco" style="left:-52px;top:330px;width:110px;height:110px;background:var(--yellow)"></span>
    <span class="deco" style="left:-30px;top:420px;width:60px;height:60px;background:var(--teal)"></span>
    <span class="deco" style="left:250px;top:380px;width:90px;height:90px;background:var(--teal);opacity:.5"></span>

    <p class="ingredients"><b>INGREDIENTS:</b><br>Water, Sugar, Ginger, Lime Juice, Gummi Arabicum, Carbonisation.</p>
    <p class="nutri-title">NUTRITION INFORMATION PER 100ml</p>
    <table class="nutri-table">
      <tr><td>Energy</td><td>74 kJ / 17 kcal</td></tr>
      <tr><td>Fat</td><td>0 g</td></tr>
      <tr class="sub"><td>– Saturated Fat</td><td>0 g</td></tr>
      <tr><td>Carbohydrates</td><td>4.1 g</td></tr>
      <tr class="sub"><td>– Sugars</td><td>3.8 g</td></tr>
      <tr><td>Protein</td><td>0 g</td></tr>
      <tr><td style="border-bottom:none">Salt</td><td style="border-bottom:none">0 g</td></tr>
    </table>
    <div class="address">
      <svg viewBox="0 0 14 18"><path d="M7 1C3.7 1 1 3.6 1 6.9 1 11 7 17 7 17S13 11 13 6.9C13 3.6 10.3 1 7 1Z" fill="#4ea56b"/><circle cx="7" cy="7" r="2.3" fill="#f8f6ea"/></svg>
      <p>Quiet Meadow Drinks<br>Lindenweg 42<br>4052 Basel<br>Switzerland</p>
    </div>
    <div class="back-rule"></div>
    <div class="cert-row">
      <div class="cert"><div class="cert-shape" style="border-radius:50%;background:var(--green)"></div>RECYCLE</div>
      <div class="cert"><div class="cert-shape" style="border-radius:50%;border:2px solid var(--green)"></div>VEGAN</div>
      <div class="cert"><div class="cert-shape" style="width:48px;background:var(--lime)"></div>BIO</div>
    </div>
  </div>

  <div class="front-panel">
    <span class="deco" style="left:-30px;top:-50px;width:150px;height:150px;background:var(--teal)"></span>
    <span class="deco" style="left:150px;top:-70px;width:140px;height:140px;background:var(--lime);opacity:.85"></span>
    <span class="deco" style="left:300px;top:0;width:110px;height:110px;background:var(--yellow);opacity:.8"></span>
    <span class="deco" style="left:-50px;top:140px;width:110px;height:110px;background:var(--mint)"></span>
    <span class="deco" style="left:318px;top:180px;width:110px;height:110px;background:var(--teal)"></span>
    <span class="deco" style="left:-40px;top:280px;width:90px;height:90px;background:var(--yellow)"></span>
    <span class="deco" style="left:-10px;top:370px;width:110px;height:110px;background:var(--mint);opacity:.7"></span>
    <span class="deco" style="left:280px;top:370px;width:120px;height:120px;background:var(--yellow)"></span>

    <div class="brand-disc"></div>
    <h2 class="brand-name">QUIET<br>MEADOW<br>DRINKS</h2>
    <p class="flavour">GINGER LIME</p>
    <div class="badge-row">
      <div class="badge"><strong>0.0%</strong><small>ALCOHOL</small></div>
      <div class="fruit-art" role="img" aria-label="Illustration of a ginger root with a lime slice"></div>
      <div class="badge bio"><strong>BIO</strong></div>
    </div>
    <p class="product-band">BIO GINGER-LIME<br>SPARKLING DRINK</p>
    <p class="volume">330ml ℮</p>
  </div>
</section>

</body>
</html>
```